Letterhead Design Needed for Real Estate Office

We are a boutique real estate agency focused on property management. We need a letter head which is professional looking and include the following information:

Logo
ABN Number
Address
Postal Address
Phone
Fax
Mobile
Email
Website

Please note that the PLVAQT logo can not be changed and must be positioned at the bottom right corner.

Please find attached the existing letterhead design for all the required elements.

Target Market(s)

Letterhead mostly used for service of notices, business letters, clients communication

Industry/Entity Type

Boutique

Colors

Designer to choose colors to be used in the design.

Requirements
Must have
• Logo

```html
<!DOCTYPE html>
<html lang="en">
<head>
<meta charset="utf-8">
<title>Northvale Partners Letterhead</title>
<link href="https://fonts.googleapis.com/css2?family=Open+Sans:wght@400;600;700&family=Noto+Sans+SC:wght@500&display=swap" rel="stylesheet">
<style>
  :root {
    --bg: #ffffff;
    --page: #ffffff;
    --page-edge: #d9d9d9;
    --ink: #1e1e1e;
    --rule: #a8c23a;
    --leaf-light: #d2e09e;
    --leaf-mid: #b5d09f;
    --brand-green: #6fa03c;
    --member-blue: #1f5f8f;
  }
  * { margin: 0; padding: 0; box-sizing: border-box; }
  html, body { width: 1200px; height: 1000px; overflow: hidden; background: var(--bg); }
  body { position: relative; font-family: "Open Sans", Arial, sans-serif; color: var(--ink); }

  .sheet {
    position: absolute; left: 304px; top: 72px; width: 595px; height: 842px;
    background: var(--page); border: 1px solid var(--page-edge);
    box-shadow: 4px 5px 8px rgba(0,0,0,0.12);
  }
  .corner-accent {
    position: absolute; right: 0; top: 0; width: 88px; height: 262px;
    background: linear-gradient(180deg, var(--leaf-light), var(--leaf-mid));
  }

  .brand { position: absolute; left: 27px; top: 38px; display: flex; align-items: center; gap: 10px; }
  .brand-square { width: 38px; height: 38px; background: var(--brand-green); }
  .brand-text { display: flex; flex-direction: column; }
  .brand-name { font-weight: 700; font-size: 17px; letter-spacing: 0.5px; line-height: 1.1; color: var(--ink); }
  .brand-name-cn { font-family: "Noto Sans SC", sans-serif; font-weight: 500; font-size: 13px; margin-top: 3px; }

  .contact { position: absolute; left: 27px; top: 711px; width: 315px; border-top: 1px solid var(--rule); padding-top: 8px; }
  .contact-row { display: flex; font-size: 8.4px; line-height: 12px; }
  .contact-label { width: 26px; flex: none; text-align: right; font-weight: 700; padding-right: 8px; border-right: 1px solid var(--rule); margin-right: 6px; }
  .contact-value { white-space: nowrap; }
  .contact-value.web { font-weight: 600; }

  .member { position: absolute; left: 446px; top: 760px; display: flex; align-items: center; gap: 8px; }
  .member-square { width: 22px; height: 22px; background: var(--member-blue); }
  .member-name { font-weight: 600; font-size: 22px; letter-spacing: -0.5px; color: var(--member-blue); }
</style>
</head>
<body>
  <main class="sheet">
    <div class="corner-accent" role="img" aria-label="Decorative corner graphic in soft green tones"></div>

    <header class="brand">
      <div class="brand-square"></div>
      <div class="brand-text">
        <span class="brand-name">NORTHVALE PARTNERS</span>
        <span class="brand-name brand-name-cn">北谷地產</span>
      </div>
    </header>

    <footer class="contact">
      <div class="contact-row"><span class="contact-label">A</span><span class="contact-value">Shop 12B 210-230 Harbour Lane Willowby NSW 2090 AUSTRALIA</span></div>
      <div class="contact-row"><span class="contact-label"></span><span class="contact-value">PO BOX 415 Willowby NSW 2091</span></div>
      <div class="contact-row"><span class="contact-label">M</span><span class="contact-value">0400 555 123</span></div>
      <div class="contact-row"><span class="contact-label">P</span><span class="contact-value">9555 0142</span></div>
      <div class="contact-row"><span class="contact-label">F</span><span class="contact-value">9555 0199</span></div>
      <div class="contact-row"><span class="contact-label">E</span><span class="contact-value">info@nvpre.example</span></div>
      <div class="contact-row"><span class="contact-label">W</span><span class="contact-value web">http://nvpre.example</span></div>
      <div class="contact-row"><span class="contact-label">ABN</span><span class="contact-value">12 345 678 901</span></div>
    </footer>

    <aside class="member">
      <div class="member-square"></div>
      <span class="member-name">PLVAQT</span>
    </aside>
  </main>
</body>
</html>
```